Promotion for Mobile Tyre Fitting on our site

We need a promotion banner to advertise mobile tyre fitting.
We sell tyres. Now we also sell a service where a mobile tyre fitter will come to the customers workplace or home and fit the tyres. This service is currently available in Brisbane and Melbourne
Benfits to the customer
It is fast and convenient.
No travel time
No wait time
Fast - usually complete within 30 minutes.
Save money by buying online
Save time
The banner should be designed so we can add more locations as they become available.
A graphic showing tyres being fitted on a car at a suburban house, or in an office car park may be appropriate. Or some kind of stylised graphic indicating the message that we come to you.
www.lowtreadhub.com.au is our site. Please look at the existing banners to ensure you create banners of the correct size. You can see a large banner beside the video and smaller banner under the Wheel Picker. We want both sizes.
Updates
Project Deadline Extended
Reason: Something has come up so I don't have time today to check progress and provide feedback so I am extending by 1 day.
I want to be fair and not leave feedback till the last minute.
I hope this doesn't cause any inconvenience.
thanks
Kev

```html
<!DOCTYPE html>
<html lang="en">
<head>
<meta charset="utf-8">
<title>Mobile Tyre Fitting Banner</title>
<link rel="stylesheet" href="https://fonts.googleapis.com/css2?family=Lato:wght@400;700;900&display=swap">
<style>
  :root {
    --text-white: #ffffff;
    --scene-top: #3b2f29;
    --scene-house: #6a4d3d;
    --scene-car: #9a9892;
    --scene-drive: #6f6a5f;
    --scene-lawn: #44502f;
    --scene-bottom: #2c3320;
    --shade: rgba(20, 14, 10, 0.55);
  }
  html, body {
    margin: 0;
    padding: 0;
    width: 1200px;
    height: 884px;
    overflow: hidden;
    background: #ffffff;
  }
  .banner {
    position: relative;
    width: 1200px;
    height: 884px;
    overflow: hidden;
    font-family: "Lato", Arial, sans-serif;
    color: var(--text-white);
  }
  .banner__scene {
    position: absolute;
    inset: 0;
    background:
      linear-gradient(180deg, var(--shade) 0%, rgba(20,14,10,0.25) 32%, rgba(0,0,0,0) 50%),
      linear-gradient(100deg, rgba(0,0,0,0.15) 0%, rgba(0,0,0,0) 40%),
      linear-gradient(180deg,
        var(--scene-top) 0%,
        var(--scene-house) 25%,
        var(--scene-car) 48%,
        var(--scene-drive) 66%,
        var(--scene-lawn) 80%,
        var(--scene-bottom) 100%);
  }
  .banner__title {
    position: absolute;
    left: 30px;
    top: 118px;
    margin: 0;
    font-size: 86px;
    font-weight: 900;
    letter-spacing: 1px;
    line-height: 1;
    white-space: nowrap;
    text-shadow: 2px 2px 6px rgba(0,0,0,0.5);
  }
  .banner__locations {
    position: absolute;
    left: 34px;
    top: 248px;
    margin: 0;
    font-size: 41px;
    font-weight: 900;
    letter-spacing: 1px;
    line-height: 1;
    text-shadow: 2px 2px 5px rgba(0,0,0,0.5);
  }
  .banner__benefits {
    position: absolute;
    left: 52px;
    top: 432px;
    margin: 0;
    padding: 0;
    list-style: none;
    font-size: 54px;
    font-weight: 400;
    line-height: 93px;
    text-shadow: 2px 2px 5px rgba(0,0,0,0.55);
  }
  .banner__benefits li::before {
    content: "";
    display: inline-block;
    width: 16px;
    height: 16px;
    border-radius: 50%;
    background: var(--text-white);
    margin-right: 24px;
    vertical-align: middle;
    position: relative;
    top: -4px;
  }
  .banner__site {
    position: absolute;
    left: 0;
    right: 0;
    bottom: 26px;
    margin: 0;
    text-align: center;
    font-size: 52px;
    font-weight: 400;
    letter-spacing: 0.5px;
    text-shadow: 2px 2px 5px rgba(0,0,0,0.55);
  }
</style>
</head>
<body>
  <main class="banner">
    <div class="banner__scene" role="img" aria-label="Suburban house driveway with a silver car having a tyre fitted by a mobile technician while a parent and child watch on the lawn"></div>
    <h1 class="banner__title">MOBILE TYRE FITTING</h1>
    <p class="banner__locations">BRISBANE &amp; MELBOURNE</p>
    <ul class="banner__benefits">
      <li>EASIER</li>
      <li>FASTER</li>
      <li>CHEAPER</li>
    </ul>
    <p class="banner__site">www.lowtreadhub.com.au</p>
  </main>
</body>
</html>
```